Design a New Business Card for Our Company

We are looking for fresh, unique, and a modern business card that reflects our roots as digital marketing agency focused on SEM.

Industry/Entity Type

Marketing

Contact Information for Business Card

looking for very unique out of the box designs. clean and modern that compliments our logo

Requirements
Must have
• colors should match our logo
• Front should have name, address, email, and phone/fax of the person, phone/fax are the same number
• back should have our url

```html
<!DOCTYPE html>
<html lang="en">
<head>
<meta charset="utf-8">
<title>Brightwave Solutions – Business Card</title>
<link rel="stylesheet" href="https://fonts.googleapis.com/css2?family=Source+Sans+3:wght@400;600&display=swap">
<style>
  :root {
    --backdrop: #121212;
    --card: #ffffff;
    --brand-blue: #4a86c8;
    --brand-grey: #a9a9a9;
    --text-grey: #555555;
    --mark-light: #dbe7f4;
  }
  * { margin: 0; padding: 0; box-sizing: border-box; }
  html, body {
    width: 1200px; height: 900px; overflow: hidden;
    background: var(--backdrop);
    font-family: "Source Sans 3", "Myriad Pro", Arial, sans-serif;
  }
  .stage { position: relative; width: 1200px; height: 900px; }
  .card {
    position: absolute; top: 306px;
    width: 440px; height: 271px;
    background: var(--card);
    border-radius: 12px;
  }
  .card--front { left: 149px; }
  .card--back { left: 608px; }

  /* front */
  .front-mark {
    position: absolute; left: 66px; top: 58px;
    width: 112px; text-align: center;
  }
  .front-mark__dot {
    display: block; width: 96px; height: 96px; margin: 0 auto 12px;
    border-radius: 50%; background: var(--brand-blue);
  }
  .front-mark__name {
    font-size: 15px; font-weight: 600; color: var(--brand-grey);
  }
  .details { position: absolute; left: 227px; top: 61px; color: var(--text-grey); }
  .details__name {
    font-size: 16px; font-weight: 600; color: var(--brand-blue); line-height: 19px;
  }
  .details__role { font-size: 13px; line-height: 15px; }
  .details__address { margin-top: 11px; font-size: 13px; line-height: 16px; }
  .contacts { margin-top: 11px; list-style: none; font-size: 13px; line-height: 16px; }
  .contacts li { display: flex; align-items: center; }
  .contacts svg { width: 9px; height: 9px; margin-right: 7px; fill: var(--brand-blue); }

  /* back */
  .wordmark {
    position: absolute; left: 0; right: 0; top: 112px;
    display: flex; align-items: center; justify-content: center; gap: 12px;
  }
  .wordmark__dot {
    width: 34px; height: 34px; border-radius: 50%; background: var(--brand-blue);
  }
  .wordmark__name {
    font-size: 36px; font-weight: 600; color: var(--brand-grey); letter-spacing: -0.5px;
  }
</style>
</head>
<body>
<main class="stage">
  <section class="card card--front" aria-label="Business card front">
    <div class="front-mark">
      <span class="front-mark__dot"></span>
      <span class="front-mark__name">Brightwave</span>
    </div>
    <div class="details">
      <p class="details__name">Daniel Carter</p>
      <p class="details__role">Managing Director</p>
      <p class="details__address">12345, Address Goes Here<br>Country Name, 123456.</p>
      <ul class="contacts">
        <li><svg viewBox="0 0 10 10" aria-hidden="true"><path d="M2 0.5l2 2-1 1.2c.6 1.2 1.6 2.2 2.8 2.8l1.2-1 2 2-1.2 1.5C4.5 9 1 5.5 .5 1.7z"/></svg>044-555 210 384</li>
        <li><svg viewBox="0 0 10 10" aria-hidden="true"><path d="M2.5 0h5v3h-5zM0 3.5h10v5H8V7H2v1.5H0zM2 7.5h6V10H2z"/></svg>044-555 210 384</li>
        <li><svg viewBox="0 0 10 10" aria-hidden="true"><path d="M0 2h10v.8L5 5.8 0 2.8zM0 3.8l5 3 5-3V8H0z"/></svg>info@brightwave.com</li>
        <li><svg viewBox="0 0 10 10" aria-hidden="true"><circle cx="5" cy="5" r="5"/></svg>www.brightwave.com</li>
      </ul>
    </div>
  </section>

  <section class="card card--back" aria-label="Business card back">
    <div class="wordmark">
      <span class="wordmark__dot"></span>
      <span class="wordmark__name">Brightwave Solutions</span>
    </div>
  </section>
</main>
</body>
</html>
```